Background image for shipboard SCADA

Need a background graphic to be used for an industrial SCADA front page, for an automation system ued on board ships.
The SCADA system is for an energy saving system, reducing electrical consumption to cooling water pumps and engine room fans.

Intention is, that the front page should give the engineers a simple overview of the system, shown on an illustration of the vessel (this series of the project is for a range of Bulk carriers, hence we prefer a bulk carrier ship).
It should be clear and simple to gain the overview, yet the look is to be professional.

As overlay on the background image, we will place text-labels contained in text-boxes with a suitable background color. Those text-boxes will show values like:
- System status (will show "Normal"/"Bypassed"/"Alarm"/"Critical alarm")
- Pumps current saving (will show "XX %")
- Fans current saving (will show "XX %")
- Total current saving (will show "XX %")
- Current energy saving (will show "XXX kW")
- Current fuel saving (will show "XXXX kg/day")

Example photo of one of the ships: https://www.harbolintrack.net/ship-photos/553018

Resolution to be: 1280 x 700 px
The monitor is a 10.1" touch-screen with black edges, mounted in a gray industrial control panel.

Target Market(s)

Multi-cultural marine engineers and ratings

Industry/Entity Type

Maritime ships

Requirements
Must have
• Simple overview for the operator, elegang design, easy to gain overview at first glance
Should not have
• Should NOT look like something from "The Quorvel"-movie

```html
<!DOCTYPE html>
<html lang="en">
<head>
<meta charset="utf-8">
<title>Shipboard Energy Saving SCADA – Front Page</title>
<link rel="stylesheet" href="https://fonts.googleapis.com/css2?family=Inter:wght@300;400;500&display=swap">
<style>
  :root {
    --page: #ffffff;
    --frame: #212b2b;
    --card: #2c3e50;
    --card-edge: #34495e;
    --sketch: #d6d7d9;
    --red: #c0392b;
    --red-dark: #96281b;
    --green: #27ae60;
    --green-dark: #1e8c4c;
    --blue: #3498db;
    --blue-dark: #2a7ab0;
    --yellow: #f39c1f;
    --yellow-dark: #c27c17;
    --purple: #8e4a9e;
    --purple-dark: #6c3583;
    --teal: #1fa38a;
    --teal-dark: #178470;
    --orange: #e67e22;
    --orange-dark: #bb6419;
    --rust: #d35427;
    --rust-dark: #a8421b;
    --ink: #ffffff;
  }
  * { box-sizing: border-box; margin: 0; padding: 0; }
  html, body { width: 1200px; height: 1200px; overflow: hidden; background: var(--page); }
  body { position: relative; font-family: "Inter", sans-serif; color: var(--ink); }

  .screen { position: absolute; left: 160px; top: 360px; width: 880px; height: 481px; background: var(--frame); }
  .card { position: absolute; background: var(--card); border: 1px solid var(--card-edge); border-radius: 10px; }
  .card--status { left: 25px; top: 25px; width: 282px; height: 430px; }
  .card--savings { left: 320px; top: 25px; width: 535px; height: 430px; }

  .placeholder { position: absolute; border-radius: 5px; }
  .vessel-outline { left: 9px; top: 9px; width: 264px; height: 89px; background: var(--sketch); }
  .vessel-photo { left: 9px; top: 9px; width: 516px; height: 138px;
    background: linear-gradient(180deg, #8a8f8c 0%, #6e7371 45%, #3f4442 100%); }

  .status-bar { position: absolute; left: 11px; top: 109px; width: 262px; height: 37px;
    background: var(--red); border-radius: 4px; font-size: 14px; letter-spacing: .3px;
    display: flex; align-items: center; justify-content: center; }

  .state { position: absolute; width: 125px; height: 126px; border-radius: 4px; }
  .state svg { position: absolute; left: 50%; top: 28px; transform: translateX(-50%); }
  .state__label { position: absolute; left: 9px; right: 9px; bottom: 10px; height: 38px; border-radius: 2px;
    display: flex; align-items: center; justify-content: center; font-size: 11px; letter-spacing: .3px; }
  .state--normal { left: 11px; top: 157px; background: var(--green); }
  .state--normal .state__label { background: var(--green-dark); }
  .state--bypassed { left: 147px; top: 157px; background: var(--blue); }
  .state--bypassed .state__label { background: var(--blue-dark); }
  .state--alarm { left: 11px; top: 295px; background: var(--yellow); }
  .state--alarm .state__label { background: var(--yellow-dark); }
  .state--critical { left: 147px; top: 295px; background: var(--red); }
  .state--critical .state__label { background: var(--red-dark); }

  .metric { position: absolute; border-radius: 4px; overflow: hidden; }
  .metric__head { height: 38px; display: flex; align-items: center; justify-content: center;
    font-size: 11px; letter-spacing: .3px; position: relative; }
  .metric__head svg { position: absolute; left: 18px; top: 9px; }
  .metric__body { height: 88px; display: flex; align-items: center; position: relative; }
  .metric__body svg { position: absolute; left: 18px; top: 26px; }
  .metric__value { font-weight: 300; font-size: 28px; position: absolute; left: 82px; top: 24px; }

  .metric--pumps { left: 9px; top: 157px; width: 164px; height: 126px; background: var(--purple); }
  .metric--pumps .metric__head { background: var(--purple-dark); }
  .metric--fans { left: 184px; top: 157px; width: 164px; height: 126px; background: var(--blue); }
  .metric--fans .metric__head { background: var(--blue-dark); }
  .metric--total { left: 360px; top: 157px; width: 164px; height: 126px; background: var(--teal); }
  .metric--total .metric__head { background: var(--teal-dark); }

  .metric--energy { left: 9px; top: 295px; width: 247px; height: 126px; background: var(--orange); }
  .metric--energy .metric__head { background: var(--orange-dark); }
  .metric--fuel { left: 268px; top: 295px; width: 257px; height: 126px; background: var(--rust); }
  .metric--fuel .metric__head { background: var(--rust-dark); }
  .metric--wide .metric__body { justify-content: center; font-weight: 300; font-size: 28px; }
</style>
</head>
<body>
<main class="screen">
  <section class="card card--status">
    <div class="placeholder vessel-outline" role="img" aria-label="Line drawing of a bulk carrier in side profile"></div>
    <div class="status-bar">SYSTEM STATUS</div>

    <div class="state state--normal">
      <svg width="24" height="28" viewBox="0 0 24 28" fill="none" stroke="#fff" stroke-width="2.2" stroke-linecap="round"><path d="M12 3v2M5 22V13a7 7 0 0 1 14 0v9M2 22h20M10 25.5h4"/></svg>
      <div class="state__label">NORMAL</div>
    </div>
    <div class="state state--bypassed">
      <svg width="24" height="28" viewBox="0 0 24 28" fill="none" stroke="#fff" stroke-width="2.2" stroke-linecap="round"><path d="M12 3v2M5 22V13a7 7 0 0 1 14 0v9M2 22h20M10 25.5h4M12 11v7M8.5 14.5h7"/></svg>
      <div class="state__label">BYPASSED</div>
    </div>
    <div class="state state--alarm">
      <svg width="24" height="28" viewBox="0 0 24 28" fill="none" stroke="#fff" stroke-width="2.2" stroke-linecap="round"><path d="M12 3v2M5 22V13a7 7 0 0 1 14 0v9M2 22h20M10 25.5h4M12 11v5M12 19v.5"/></svg>
      <div class="state__label">ALARM</div>
    </div>
    <div class="state state--critical">
      <svg width="32" height="28" viewBox="0 0 32 28" fill="none" stroke="#fff" stroke-width="2.2" stroke-linecap="round"><path d="M16 3v2M9 22V13a7 7 0 0 1 14 0v9M6 22h20M14 25.5h4M5 7a12 12 0 0 0-2 8M27 7a12 12 0 0 1 2 8"/></svg>
      <div class="state__label">CRITICAL ALARM</div>
    </div>
  </section>

  <section class="card card--savings">
    <div class="placeholder vessel-photo" role="img" aria-label="Photograph of a bulk carrier at anchor on calm grey water"></div>

    <div class="metric metric--pumps">
      <div class="metric__head">PUMPS CURRENT SAVING</div>
      <div class="metric__body">
        <svg width="42" height="38" viewBox="0 0 42 38" fill="none" stroke="#fff" stroke-width="1.6"><rect x="8" y="10" width="22" height="18" rx="2"/><path d="M30 13h6v12h-6M2 14h6M2 24h6M2 12v14M14 4h8v6M12 2h12M4 34h34M10 28v6M28 28v6M12 14v10M16 14v10M20 14v10M24 14v10"/></svg>
        <span class="metric__value">XX%</span>
      </div>
    </div>
    <div class="metric metric--fans">
      <div class="metric__head">FANS CURRENT SAVING</div>
      <div class="metric__body">
        <svg width="38" height="38" viewBox="0 0 38 38" fill="none" stroke="#fff" stroke-width="1.6"><circle cx="19" cy="19" r="3"/><path d="M19 16c-5-1-7-6-5-10s9-3 9 2-2 6-4 8zM22 19c1-5 6-7 10-5s3 9-2 9-6-2-8-4zM19 22c5 1 7 6 5 10s-9 3-9-2 2-6 4-8zM16 19c-1 5-6 7-10 5s-3-9 2-9 6 2 8 4z"/></svg>
        <span class="metric__value">XX%</span>
      </div>
    </div>
    <div class="metric metric--total">
      <div class="metric__head">TOTAL CURRENT SAVING</div>
      <div class="metric__body">
        <svg width="36" height="40" viewBox="0 0 36 40" fill="none" stroke="#fff" stroke-width="1.6" stroke-linejoin="round"><path d="M24 2L4 24h13l-5 14 20-22H19z"/></svg>
        <span class="metric__value">XX%</span>
      </div>
    </div>

    <div class="metric metric--wide metric--energy">
      <div class="metric__head">
        <svg width="21" height="21" viewBox="0 0 21 21" fill="none" stroke="var(--orange)" stroke-width="1.8" stroke-linejoin="round"><circle cx="10.5" cy="10.5" r="9"/><path d="M12 4l-5 8h4l-2 5 5-8h-4z" fill="var(--orange)"/></svg>
        CURRENT ENERGY SAVING
      </div>
      <div class="metric__body">XXXkW</div>
    </div>
    <div class="metric metric--wide metric--fuel">
      <div class="metric__head">
        <svg width="22" height="22" viewBox="0 0 22 22" fill="none" stroke="var(--rust)" stroke-width="1.8"><path d="M3 1h16M3 21h16M5 1v20M17 1v20M2 5h3M2 17h3M17 5h3M17 17h3"/><path d="M11 7c-2 3-3 4-3 6a3 3 0 0 0 6 0c0-2-1-3-3-6z" fill="var(--rust)"/></svg>
        CURRENT FUEL SAVING
      </div>
      <div class="metric__body">XXXX kg/day</div>
    </div>
  </section>
</main>
</body>
</html>
```